Remote Planning & Scheduling Power Point Presentation

This PP presentation is to help explain what RPS is and its benefits. Need help with a better illustration on slide 3 that explains the process, overall aesthetics, need better images, and cleaner workflow on slide 18. Keep the ZOL Logo in the bottom right of each slide. I have included a one-pager and infographic to help. I am still working of verbiage.

Thanks
JR

```html
<!DOCTYPE html>
<html lang="en">
<head>
<meta charset="utf-8">
<title>ZOL – Remote Planning &amp; Scheduling deck</title>
<link href="https://fonts.googleapis.com/css2?family=Exo+2:wght@400;500;600;700&family=Barlow:wght@400;500;600&display=swap" rel="stylesheet">
<style>
  :root{
    --page:#f3f4f7;
    --slide:#ffffff;
    --navy:#12338f;
    --navy-deep:#0c2a7e;
    --cover-top:#2c4fa6;
    --cover-bottom:#1d3c92;
    --heading:#163a9c;
    --body:#4a4f5c;
    --muted:#9aa6c0;
    --mark:#cdd5e6;
    --rail:#eceef2;
    --sky:#6cc7ee;
    --orange:#f07a2a;
    --green:#4ccf97;
    --illus:#e4eaf5;
  }
  html,body{margin:0;padding:0;}
  body{
    width:716px;height:1200px;overflow:hidden;
    background:var(--page);position:relative;
    font-family:"Barlow",sans-serif;
  }
  .slide{
    position:absolute;width:343px;height:192px;
    background:var(--slide);
    box-shadow:0 1px 4px rgba(20,40,90,.08);
    overflow:hidden;display:block;
  }
  .col-a{left:8px}
  .col-b{left:366px}
  .row-1{top:4px}.row-2{top:203px}.row-3{top:403px}
  .row-4{top:607px}.row-5{top:803px}.row-6{top:1003px}

  .heading{font-family:"Exo 2",sans-serif;font-weight:500;font-size:28px;fill:var(--heading)}
  .cover-title{font-family:"Exo 2",sans-serif;font-weight:500;font-size:29px;fill:#fff}
  .cover-year{font-family:"Exo 2",sans-serif;font-weight:500;font-size:16px;fill:#fff}
  .year-muted{font-family:"Exo 2",sans-serif;font-size:16px;fill:#c9d2e6}
  .brand{font-family:"Exo 2",sans-serif;font-weight:700;fill:#fff}
  .brand-sub{font-family:"Exo 2",sans-serif;font-weight:600;font-size:7px;fill:#fff;letter-spacing:.6px}
  .corner-mark{font-family:"Exo 2",sans-serif;font-weight:700;font-size:17px;fill:var(--mark)}
  .footer{font-family:"Barlow",sans-serif;font-size:5px;fill:var(--navy)}
  .item{font-family:"Barlow",sans-serif;font-size:11.5px;fill:var(--body)}
  .num{font-family:"Barlow",sans-serif;font-weight:600;font-size:11px;fill:#fff;text-anchor:middle}
  .num-sm{font-family:"Barlow",sans-serif;font-weight:600;font-size:8px;fill:#fff;text-anchor:middle}
  .dot{fill:var(--navy-deep)}
  .rail{fill:var(--rail)}
  .icon-tile{fill:var(--navy)}
  .glyph{fill:none;stroke:#fff;stroke-width:1.6;stroke-linecap:round;stroke-linejoin:round}

  .flow-box-solid{fill:var(--navy-deep)}
  .flow-box{fill:#fff;stroke:var(--navy-deep);stroke-width:2}
  .flow-box-sky{fill:#fff;stroke:var(--sky);stroke-width:1.5}
  .flow-box-orange{fill:#fff;stroke:var(--orange);stroke-width:1.5}
  .flow-box-green{fill:#fff;stroke:var(--green);stroke-width:1.5}
  .flow-label{font-family:"Barlow",sans-serif;font-weight:600;font-size:7.5px;text-anchor:middle}
  .lbl-white{fill:#fff}.lbl-navy{fill:var(--navy-deep)}.lbl-sky{fill:var(--sky)}
  .lbl-orange{fill:var(--orange)}.lbl-green{fill:var(--green)}
  .pipe-navy{fill:none;stroke:var(--navy-deep);stroke-width:10}
  .pipe-sky{fill:none;stroke:var(--sky);stroke-width:10}
  .pipe-orange{fill:none;stroke:var(--orange);stroke-width:10}
  .pipe-green{fill:none;stroke:var(--green);stroke-width:10}
  .link{fill:none;stroke:var(--navy-deep);stroke-width:1.2}
  .illus{fill:var(--illus)}

  .timeline{fill:none;stroke:#8a93a6;stroke-width:1;stroke-dasharray:2 2}
  .stage{font-family:"Barlow",sans-serif;font-weight:500;font-size:9px;fill:var(--navy)}
  .stage-note{font-family:"Barlow",sans-serif;font-size:5px;fill:var(--body)}
</style>
</head>
<body>

<!-- Cover, full-bleed -->
<svg class="slide col-a row-1" viewBox="0 0 710 398">
  <defs>
    <linearGradient id="coverFill" x1="0" y1="0" x2="0" y2="1">
      <stop offset="0" stop-color="#2f53a9"/>
      <stop offset="1" stop-color="#1b3a8e"/>
    </linearGradient>
  </defs>
  <rect width="710" height="398" fill="url(#coverFill)" role="img" aria-label="Refinery skyline photograph under a blue tint"/>
  <text class="brand" x="355" y="150" font-size="46" text-anchor="middle">ZOL</text>
  <text class="brand-sub" x="355" y="165" text-anchor="middle">PROJECT SERVICES, LTD.</text>
  <text class="cover-title" x="355" y="253" text-anchor="middle">Remote Planning &amp; Scheduling</text>
  <text class="cover-year" x="355" y="306" text-anchor="middle">2020</text>
  <text class="corner-mark" x="635" y="345" text-anchor="middle" style="fill:#6d86c4">ZOL</text>
</svg>

<!-- Cover, split -->
<svg class="slide col-b row-1" viewBox="0 0 710 398">
  <rect x="35" y="0" width="320" height="398" fill="url(#coverFill)" role="img" aria-label="Refinery skyline photograph under a blue tint"/>
  <text class="brand" x="195" y="215" font-size="60" text-anchor="middle">ZOL</text>
  <text class="brand-sub" x="195" y="232" text-anchor="middle" font-size="9">PROJECT SERVICES, LTD.</text>
  <text class="heading" x="407" y="113">Remote Planning</text>
  <text class="heading" x="407" y="149">&amp; Scheduling</text>
  <text class="year-muted" x="407" y="200">2020</text>
  <text class="corner-mark" x="655" y="373" text-anchor="middle">ZOL</text>
</svg>

<!-- Innovative approach -->
<svg class="slide col-a row-2" viewBox="0 0 710 398">
  <rect class="rail" x="352" y="0" width="8" height="398"/>
  <text class="heading" x="32" y="194" font-size="26">Innovative Approach</text>
  <text class="heading" x="32" y="226" font-size="26">to Planning</text>
  <circle class="dot" cx="356" cy="157" r="18"/>
  <path class="glyph" d="M347 160h18M349 160v-5h12l3 5M351 163a1.5 1.5 0 1 0 .1 0M361 163a1.5 1.5 0 1 0 .1 0"/>
  <circle class="dot" cx="356" cy="243" r="18"/>
  <path class="glyph" d="M348 250l8-8M352 238l4 4 5-5M357 247l6-6"/>
  <text class="item" x="405" y="154" font-size="12.5">No more paying for man</text>
  <text class="item" x="405" y="170" font-size="12.5">hours, buy a finished product</text>
  <text class="item" x="405" y="240" font-size="12.5">Able to focus on getting the right</text>
  <text class="item" x="405" y="256" font-size="12.5">scope, let us focus on your planning</text>
  <text class="footer" x="34" y="380">© Copyright 2020 ZOL Project Services LTD. All rights reserved | 3</text>
  <text class="corner-mark" x="653" y="385" text-anchor="middle">ZOL</text>
</svg>

<!-- RPS flow process -->
<svg class="slide col-b row-2" viewBox="0 0 710 398">
  <text class="heading" x="34" y="60">RPS Flow Process</text>
  <g role="img" aria-label="Illustrated people at work along the process">
    <rect class="illus" x="30" y="103" width="48" height="52" rx="6"/>
    <rect class="illus" x="128" y="186" width="32" height="48" rx="6"/>
    <rect class="illus" x="272" y="122" width="64" height="60" rx="6"/>
    <rect class="illus" x="452" y="104" width="54" height="46" rx="6"/>
    <rect class="illus" x="328" y="216" width="28" height="52" rx="6"/>
    <rect class="illus" x="534" y="260" width="86" height="52" rx="6"/>
    <rect class="illus" x="444" y="272" width="24" height="32" rx="4"/>
  </g>
  <path class="pipe-navy" d="M60 209V268Q60 287 80 287H207Q225 287 225 268V163"/>
  <path class="pipe-sky" d="M225 132V106Q225 90 241 90H392Q408 90 408 106V292"/>
  <path class="pipe-orange" d="M408 292V318Q408 333 422 333"/>
  <path class="pipe-green" d="M620 333H628Q640 333 640 318V154"/>
  <rect x="277" y="77" width="98" height="22" fill="var(--sky)"/>
  <text class="flow-label lbl-white" x="326" y="92">REMOTE</text>
  <rect class="flow-box-solid" x="24" y="171" width="74" height="38"/>
  <text class="flow-label lbl-white" x="61" y="193">ON SITE</text>
  <rect class="flow-box" x="23" y="231" width="85" height="29"/>
  <text class="flow-label lbl-navy" x="65" y="249">COLLECT WORKLIST</text>
  <rect class="flow-box" x="95" y="280" width="85" height="28"/>
  <text class="flow-label lbl-navy" x="137" y="297">SCOPE REVIEW</text>
  <rect class="flow-box" x="187" y="235" width="86" height="31"/>
  <text class="flow-label lbl-navy" x="230" y="253">DATA COLLECTION</text>
  <rect class="flow-box" x="171" y="132" width="86" height="31"/>
  <text class="flow-label lbl-navy" x="214" y="150">FIELD PHOTOS</text>
  <path class="link" d="M70 140h14v28M116 235v10h-8M158 315v-6M224 100v0"/>
  <rect class="flow-box-sky" x="376" y="114" width="68" height="28"/>
  <text class="flow-label lbl-sky" x="410" y="126">DETAIL</text>
  <text class="flow-label lbl-sky" x="410" y="136">PLANNING</text>
  <rect class="flow-box-sky" x="369" y="167" width="65" height="29"/>
  <text class="flow-label lbl-sky" x="401" y="179">DEVELOP</text>
  <text class="flow-label lbl-sky" x="401" y="189">PACKAGE</text>
  <rect class="flow-box-sky" x="395" y="219" width="58" height="28"/>
  <text class="flow-label lbl-sky" x="424" y="231">PACKAGE</text>
  <text class="flow-label lbl-sky" x="424" y="241">REVIEW</text>
  <circle cx="378" cy="236" r="16" fill="none" stroke="#222" stroke-width="3"/>
  <rect class="flow-box-orange" x="420" y="320" width="84" height="25"/>
  <text class="flow-label lbl-orange" x="462" y="336">LEVEL 1 SCHEDULE</text>
  <path d="M509 325l6 7-6 7M516 325l6 7-6 7M523 325l6 7-6 7" fill="none" stroke="var(--orange)" stroke-width="2"/>
  <rect class="flow-box-green" x="533" y="320" width="87" height="25"/>
  <text class="flow-label lbl-green" x="576" y="336">SCHEDULE REVIEW</text>
  <rect class="flow-box-orange" x="617" y="257" width="85" height="30"/>
  <text class="flow-label lbl-orange" x="659" y="275">LEVEL 2 SCHEDULE</text>
  <rect class="flow-box-green" x="597" y="190" width="85" height="30"/>
  <text class="flow-label lbl-green" x="639" y="208">SCHEDULE REVIEW</text>
  <rect x="603" y="116" width="70" height="38" fill="var(--green)"/>
  <text class="flow-label lbl-white" x="638" y="133">LEVEL 3</text>
  <text class="flow-label lbl-white" x="638" y="143">SCHEDULE</text>
  <path d="M638 110V86l10 5-10 5" fill="var(--green)" stroke="var(--green)" stroke-width="1.5"/>
  <text class="footer" x="34" y="380">© Copyright 2020 ZOL Project Services LTD. All rights reserved | 4</text>
  <text class="corner-mark" x="653" y="385" text-anchor="middle">ZOL</text>
</svg>

<!-- Detail planning 1 -->
<svg class="slide col-a row-3" viewBox="0 0 710 398">
  <text class="heading" x="34" y="60">Detail Planning</text>
  <rect class="rail" x="352" y="85" width="8" height="313"/>
  <circle cx="356" cy="85" r="8" fill="#fff"/>
  <g>
    <circle class="dot" cx="356" cy="130" r="13"/><text class="num" x="356" y="134">1</text>
    <circle class="dot" cx="356" cy="180" r="13"/><text class="num" x="356" y="184">2</text>
    <circle class="dot" cx="356" cy="230" r="13"/><text class="num" x="356" y="234">3</text>
    <circle class="dot" cx="356" cy="280" r="13"/><text class="num" x="356" y="284">4</text>
    <circle class="dot" cx="356" cy="330" r="13"/><text class="num" x="356" y="334">5</text>
  </g>
  <text class="item" x="405" y="134">Conducted field walk &amp; captured field notes</text>
  <text class="item" x="405" y="184">Collected field photos</text>
  <text class="item" x="405" y="228">Create job activities, identify resources,</text>
  <text class="item" x="405" y="242">estimate durations, identify TA phases</text>
  <text class="item" x="405" y="284">Annotate pictures and P&amp;ID's</text>
  <text class="item" x="405" y="334">Identify blind points (hydro, &amp; entry blinds)</text>
  <text class="footer" x="34" y="380">© Copyright 2020 ZOL Project Services LTD. All rights reserved | 5</text>
  <text class="corner-mark" x="653" y="385" text-anchor="middle">ZOL</text>
</svg>

<!-- Develop package 1 -->
<svg class="slide col-b row-3" viewBox="0 0 710 398">
  <rect class="icon-tile" x="0" y="35" width="36" height="27"/>
  <path class="glyph" d="M18 42a6 6 0 1 0 .1 0M18 46a2 2 0 1 0 .1 0"/>
  <text class="heading" x="45" y="60">Develop Package</text>
  <rect class="rail" x="351" y="85" width="8" height="313"/>
  <circle cx="355" cy="85" r="8" fill="#fff"/>
  <g>
    <circle class="dot" cx="355" cy="127" r="9"/><text class="num-sm" x="355" y="130">1</text>
    <circle class="dot" cx="355" cy="164" r="9"/><text class="num-sm" x="355" y="167">2</text>
    <circle class="dot" cx="355" cy="202" r="9"/><text class="num-sm" x="355" y="205">3</text>
    <circle class="dot" cx="355" cy="239" r="9"/><text class="num-sm" x="355" y="242">4</text>
    <circle class="dot" cx="355" cy="276" r="9"/><text class="num-sm" x="355" y="279">5</text>
    <circle class="dot" cx="355" cy="313" r="9"/><text class="num-sm" x="355" y="316">6</text>
    <circle class="dot" cx="355" cy="350" r="9"/><text class="num-sm" x="355" y="353">7</text>
  </g>
  <text class="item" x="405" y="131">P&amp;ID - mark up scope &amp; blind location</text>
  <text class="item" x="405" y="168">Plot Plan - mark up scope</text>
  <text class="item" x="405" y="206">Equip Dwgs – collect add to package</text>
  <text class="item" x="405" y="243">Equip Data Sheet - collect add to package</text>
  <text class="item" x="405" y="280">Photo - mark up and scope description</text>
  <text class="item" x="405" y="317">Safety Data Sheet - identify PPE required</text>
  <text class="item" x="405" y="354">Step Out - create job step out</text>
  <text class="footer" x="34" y="380">© Copyright 2020 ZOL Project Services LTD. All rights reserved | 7</text>
  <text class="corner-mark" x="653" y="385" text-anchor="middle">ZOL</text>
</svg>

<!-- Detail planning 2 -->
<svg class="slide col-a row-4" viewBox="0 0 710 398">
  <text class="heading" x="37" y="60">Detail Planning</text>
  <rect class="rail" x="356" y="0" width="8" height="350"/>
  <circle cx="360" cy="350" r="9" fill="#fff" stroke="var(--rail)"/>
  <g>
    <circle class="dot" cx="360" cy="48" r="13"/><text class="num" x="360" y="52">6</text>
    <circle class="dot" cx="360" cy="92" r="13"/><text class="num" x="360" y="96">7</text>
    <circle class="dot" cx="360" cy="137" r="13"/><text class="num" x="360" y="141">8</text>
    <circle class="dot" cx="360" cy="181" r="13"/><text class="num" x="360" y="185">9</text>
    <circle class="dot" cx="360" cy="229" r="13"/><text class="num" x="360" y="233">10</text>
    <circle class="dot" cx="360" cy="271" r="13"/><text class="num" x="360" y="275">11</text>
  </g>
  <text class="item" x="409" y="52">Identify PPE requirements</text>
  <text class="item" x="409" y="96">Provide safety ranking for each activity</text>
  <text class="item" x="409" y="141">Create material list</text>
  <text class="item" x="409" y="185">Create job packages</text>
  <text class="item" x="409" y="233">Capture notes at the activity level</text>
  <text class="item" x="409" y="275">Scaffold Requirements</text>
  <text class="footer" x="37" y="380">© Copyright 2020 ZOL Project Services LTD. All rights reserved | 6</text>
  <text class="corner-mark" x="656" y="385" text-anchor="middle">ZOL</text>
</svg>

<!-- Develop package 2 -->
<svg class="slide col-b row-4" viewBox="0 0 710 398">
  <rect class="icon-tile" x="0" y="35" width="36" height="27"/>
  <path class="glyph" d="M18 42a6 6 0 1 0 .1 0M18 46a2 2 0 1 0 .1 0"/>
  <text class="heading" x="45" y="60">Develop Package</text>
  <rect class="rail" x="352" y="0" width="8" height="340"/>
  <circle cx="356" cy="340" r="9" fill="#fff" stroke="var(--rail)"/>
  <g>
    <circle class="dot" cx="356" cy="49" r="9"/><text class="num-sm" x="356" y="52">8</text>
    <circle class="dot" cx="356" cy="85" r="9"/><text class="num-sm" x="356" y="88">9</text>
    <circle class="dot" cx="356" cy="121" r="9"/><text class="num-sm" x="356" y="124">10</text>
    <circle class="dot" cx="356" cy="157" r="9"/><text class="num-sm" x="356" y="160">11</text>
    <circle class="dot" cx="356" cy="193" r="9"/><text class="num-sm" x="356" y="196">12</text>
    <circle class="dot" cx="356" cy="231" r="9"/><text class="num-sm" x="356" y="234">13</text>
    <circle class="dot" cx="356" cy="268" r="9"/><text class="num-sm" x="356" y="271">14</text>
    <circle class="dot" cx="356" cy="309" r="9"/><text class="num-sm" x="356" y="312">15</text>
  </g>
  <text class="item" x="407" y="53">Blind List - create blind list</text>
  <text class="item" x="405" y="89">Material List - create material list</text>
  <text class="item" x="405" y="125">QAQC Forms - fill out planning information</text>
  <text class="item" x="405" y="161">Closure Forms - fill out planning information</text>
  <text class="item" x="405" y="197">Spec Sheets - order material according to spec</text>
  <text class="item" x="405" y="235">ITP - incorporate ITP in job plans</text>
  <text class="item" x="405" y="272">Safety Risk - Identify risk level</text>
  <text class="item" x="405" y="313">MI Reports - fill out planning information</text>
  <text class="footer" x="34" y="380">© Copyright 2020 ZOL Project Services LTD. All rights reserved | 8</text>
  <text class="corner-mark" x="653" y="385" text-anchor="middle">ZOL</text>
</svg>

<!-- Package review -->
<svg class="slide col-a row-5" viewBox="0 0 710 398">
  <rect class="icon-tile" x="0" y="36" width="36" height="27"/>
  <path class="glyph" d="M12 41h9l4 4v13H12zM19 50a3 3 0 1 0 .1 0M21 52l3 3"/>
  <text class="heading" x="47" y="60">Package Review</text>
  <text class="footer" x="34" y="380">© Copyright 2020 ZOL Project Services LTD. All rights reserved | 9</text>
  <text class="corner-mark" x="653" y="385" text-anchor="middle">ZOL</text>
</svg>

<!-- Package acceptance -->
<svg class="slide col-b row-5" viewBox="0 0 710 398">
  <rect class="icon-tile" x="0" y="36" width="36" height="27"/>
  <path class="glyph" d="M9 50l6-6 5 3 6-4 4 6-8 7-5-4z"/>
  <text class="heading" x="47" y="60">Package Acceptance</text>
  <text class="footer" x="34" y="380">© Copyright 2020 ZOL Project Services LTD. All rights reserved | 10</text>
  <text class="corner-mark" x="653" y="385" text-anchor="middle">ZOL</text>
</svg>

<!-- Schedules -->
<svg class="slide col-a row-6" viewBox="0 0 710 398">
  <rect class="icon-tile" x="0" y="36" width="36" height="27"/>
  <path class="glyph" d="M10 43h16v14H10zM10 47h16M14 41v4M22 41v4"/>
  <text class="heading" x="47" y="60">Schedules</text>
  <path class="timeline" d="M68 268V155Q68 140 83 140H182Q196 140 196 155V320Q196 332 210 332H316Q330 332 330 318V152Q330 138 345 138H448Q462 138 462 152V275Q462 290 477 290H578"/>
  <circle class="dot" cx="68" cy="268" r="2"/>
  <circle class="dot" cx="68" cy="193" r="4"/>
  <circle class="dot" cx="196" cy="258" r="4"/>
  <circle class="dot" cx="330" cy="288" r="4"/>
  <circle class="dot" cx="462" cy="152" r="4"/>
  <path d="M83 170v-10M87 170v-12M91 170v-9M95 170v-11" stroke="var(--navy)" stroke-width="1.5"/>
  <path d="M211 235v-10M215 235v-12M219 235v-9M223 235v-11" stroke="var(--navy)" stroke-width="1.5"/>
  <path d="M345 275v-10M349 275v-12M353 275v-9M357 275v-11" stroke="var(--navy)" stroke-width="1.5"/>
  <path d="M478 140a4 4 0 1 0 .1 0M475 144l-3 4" fill="none" stroke="var(--navy)" stroke-width="1.2"/>
  <text class="stage" x="82" y="196">Level 1</text>
  <text class="stage-note" x="82" y="210">•</text><text class="stage-note" x="92" y="210">Internal Logic as well</text>
  <text class="stage-note" x="92" y="216">as external logic</text>
  <text class="stage-note" x="82" y="222">•</text><text class="stage-note" x="92" y="222">Resource leveling</text>
  <text class="stage" x="210" y="261">Level 2</text>
  <text class="stage-note" x="210" y="274">•</text><text class="stage-note" x="220" y="274">Histograms</text>
  <text class="stage-note" x="210" y="280">•</text><text class="stage-note" x="220" y="280">Milestone KPI's</text>
  <text class="stage" x="344" y="291">Level 3</text>
  <text class="stage-note" x="344" y="305">•</text><text class="stage-note" x="354" y="305">Customized Reporting</text>
  <text class="stage" x="475" y="155">Schedule Reviews</text>
  <g class="stage-note">
    <text x="475" y="168">•</text><text x="485" y="168">Risk Reviewed</text>
    <text x="475" y="174">•</text><text x="485" y="174">Internal Logic only. From one Task to another</text>
    <text x="485" y="180">e.g., Blind Exchanger to Open Dollar Plate</text>
    <text x="485" y="186">etc...)</text>
    <text x="475" y="192">•</text><text x="485" y="192">Resource loaded Tasks</text>
    <text x="475" y="198">•</text><text x="485" y="198">Standard Activity Codes assigned to all Tasks</text>
    <text x="475" y="204">•</text><text x="485" y="204">Default Calendars assigned to all Activities (8</text>
    <text x="485" y="210">hours per day, 5 Days per Week) unless</text>
    <text x="485" y="216">prearranged to use a TAR calendar as the</text>
    <text x="485" y="222">default</text>
    <text x="475" y="228">•</text><text x="485" y="228">All following PMX rules for project</text>
    <text x="485" y="234">development</text>
  </g>
  <text class="footer" x="34" y="380">© Copyright 2020 ZOL Project Services LTD. All rights reserved | 11</text>
  <text class="corner-mark" x="653" y="385" text-anchor="middle">ZOL</text>
</svg>

</body>
</html>
```